BHSM Business Card Design Project

We are a Wedding Film company in Charleston, SC In need of a unique business card. Our website is www.brightharborstudiomedia.com. Check us out to get an idea of who we are and what we do. The design should be upscale but not pretentious. Modern but not cheesy. I will most likely have our cards printed by Zell on the Plume design. I'm also liking the raised designs for our logo. The Wedding Films in our logo on our site is blue so feel free to manipulate our logo for your designs as well.

Industry/Entity Type

Business

Requirements
Must have
• This is the info I want on the card:

Derek Halloway
Storyteller

Brightharbor Studio Media
www.brightharborstudiomedia.com

843.627.4150
derek@brightharborstudiomedia.com

```html
<!DOCTYPE html>
<html lang="en">
<head>
<meta charset="utf-8">
<title>Brightharbor Studio Media – Business Card</title>
<link rel="stylesheet" href="https://fonts.googleapis.com/css2?family=Cinzel:wght@500;600&family=Open+Sans:wght@400;600;700&display=swap">
<style>
  :root {
    --stage: #000000;
    --card-white: #ffffff;
    --brand-gold: #a5885a;
    --gold-light: #d9c48f;
    --gold-mid: #a88c59;
    --gold-deep: #7e6a43;
    --ink-light: #ffffff;
  }
  * { margin: 0; padding: 0; box-sizing: border-box; }
  html, body {
    width: 1200px; height: 1200px; overflow: hidden;
    background: var(--stage);
  }
  .canvas { position: relative; width: 1200px; height: 1200px; }

  .card {
    position: absolute; left: 414px; width: 382px; height: 234px;
    overflow: hidden;
  }

  /* Front */
  .card-front { top: 247px; background: var(--card-white); }
  .brand-mark {
    position: absolute; left: 50%; top: 62px; transform: translateX(-50%);
    width: 46px; height: 46px; border-radius: 50%;
    background: var(--brand-gold);
  }
  .brand-name {
    position: absolute; left: 0; right: 0; top: 124px; text-align: center;
    font-family: "Open Sans", sans-serif; font-weight: 600;
    font-size: 21px; letter-spacing: 0.3px; color: var(--brand-gold);
  }

  /* Back */
  .card-back {
    top: 511px;
    background: radial-gradient(ellipse 70% 80% at 18% 18%, var(--gold-light) 0%, var(--gold-mid) 55%, var(--gold-deep) 100%);
  }
  .back-decoration {
    position: absolute; right: 0; top: 0; width: 150px; height: 234px;
    background: linear-gradient(100deg, rgba(255,240,200,0) 0%, rgba(255,240,200,0.14) 55%, rgba(255,240,200,0.22) 100%);
  }
  .contact {
    position: absolute; left: 0; right: 0; top: 78px; text-align: center;
    color: var(--ink-light);
  }
  .contact-name {
    font-family: "Cinzel", serif; font-weight: 600;
    font-size: 17px; letter-spacing: 0.8px; line-height: 20px;
  }
  .contact-role {
    font-family: "Cinzel", serif; font-weight: 500;
    font-size: 12px; letter-spacing: 0.6px; line-height: 16px;
  }
  .contact-email, .contact-phone, .contact-web {
    font-family: "Open Sans", sans-serif; font-size: 11.5px; line-height: 14px;
  }
  .contact-email { margin-top: 18px; }
  .contact-phone { margin-top: 10px; font-weight: 700; font-size: 12px; }
  .contact-web { margin-top: 10px; }
</style>
</head>
<body>
<main class="canvas">
  <section class="card card-front">
    <span class="brand-mark" aria-hidden="true"></span>
    <p class="brand-name">Brightharbor Studio Media</p>
  </section>

  <section class="card card-back">
    <div class="back-decoration" role="img" aria-label="Faint embossed tree motif in light gold"></div>
    <div class="contact">
      <p class="contact-name">Derek Halloway</p>
      <p class="contact-role">Storyteller</p>
      <p class="contact-email">derek@brightharborstudiomedia.com</p>
      <p class="contact-phone">843.627.4150</p>
      <p class="contact-web">www.brightharborstudiomedia.com</p>
    </div>
  </section>
</main>
</body>
</html>
```